Real Estate Entrepreneur needs a business card

I am a real estate entrepreneur, I buy houses for investment purposes, I act as a real estate agent representing buyers and sellers in residential home transactions, I am a contractor that does a wide range of home repairs and construction. I'd like a design that can stick with me through the years as my business grows and morphs to fit any niche I decide to pursue as markets change.

Target Market(s)

Anyone with interest that may be related to real estate.

Industry/Entity Type

Real Estate

Contact Information for Business Card

A card that stands out and doesn't put me in any one box. My business will evolve over time and I need a card that can stay relevant.

Colors

Designer to choose colors to be used in the design.

Requirements
Must have
• Character
Nice to have
• I'm open
Should not have
• Cliche houses and hammers

```html
<!DOCTYPE html>
<html lang="en">
<head>
<meta charset="utf-8">
<title>Reid Calloway — Business Card</title>
<link rel="stylesheet" href="https://fonts.googleapis.com/css2?family=Michroma&family=Montserrat:wght@500&display=swap">
<style>
  :root {
    --backdrop: #ececec;
    --card-ink: #151c24;
    --accent-blue: #5b7a90;
    --accent-grey: #8a8c8f;
    --text-grey: #8e9195;
  }
  html, body {
    margin: 0;
    padding: 0;
    width: 1200px;
    height: 1200px;
    overflow: hidden;
    background: var(--backdrop);
  }
  .canvas {
    position: relative;
    width: 1200px;
    height: 1200px;
  }
  .card {
    position: absolute;
    left: 350px;
    width: 528px;
    height: 301px;
    display: block;
  }
  .card--front { top: 325px; }
  .card--back { top: 670px; }
  .card-base { fill: var(--card-ink); }
  .accent-zone--front { fill: url(#accentFront); }
  .accent-zone--back { fill: url(#accentBack); }
  .brand-name {
    font-family: "Michroma", sans-serif;
    font-size: 37px;
    fill: var(--text-grey);
    letter-spacing: 1px;
  }
  .brand-role {
    font-family: "Michroma", sans-serif;
    font-size: 9px;
    fill: var(--text-grey);
    letter-spacing: 4.4px;
  }
  .contact-line {
    font-family: "Montserrat", sans-serif;
    font-weight: 500;
    font-size: 13px;
    fill: var(--text-grey);
    letter-spacing: 0.6px;
  }
  .contact-icon { fill: var(--text-grey); }
</style>
</head>
<body>
<main class="canvas">

  <svg class="card card--front" viewBox="0 0 659 376" aria-label="Business card front">
    <defs>
      <linearGradient id="accentFront" x1="0" y1="0" x2="1" y2="1">
        <stop offset="0" stop-color="var(--accent-blue)"/>
        <stop offset="1" stop-color="var(--accent-grey)"/>
      </linearGradient>
    </defs>
    <rect class="card-base" width="659" height="376"/>
    <polygon class="accent-zone--front" role="img" aria-label="Diagonal decorative graphic in blue and grey"
             points="0,0 165,0 273,181 215,181 332,376 0,376"/>
    <text class="brand-name" x="268" y="219" textLength="326" lengthAdjust="spacingAndGlyphs">REID CALLOWAY</text>
    <text class="brand-role" x="269" y="240" textLength="325" lengthAdjust="spacingAndGlyphs">REAL ESTATE ENTREPRENEUR</text>
  </svg>

  <svg class="card card--back" viewBox="0 0 659 376" aria-label="Business card back">
    <defs>
      <linearGradient id="accentBack" x1="1" y1="0" x2="0" y2="1">
        <stop offset="0" stop-color="var(--accent-blue)"/>
        <stop offset="1" stop-color="var(--accent-grey)"/>
      </linearGradient>
    </defs>
    <rect class="card-base" width="659" height="376"/>
    <polygon class="accent-zone--back" role="img" aria-label="Diagonal decorative graphic in blue and grey"
             points="492,0 659,0 659,376 327,376 458,181 374,181"/>

    <g class="contact">
      <path class="contact-icon" d="M179,182 a5,5 0 0 1 5,5 c0,4 -5,9 -5,9 c0,0 -5,-5 -5,-9 a5,5 0 0 1 5,-5 z M179,185 a2,2 0 1 0 0.01,0 z" fill-rule="evenodd"/>
      <text class="contact-line" x="202" y="197">123 Dummy, Lorem , Country</text>

      <path class="contact-icon" d="M175,212 l3,-1 l2,4 l-2,1.5 c1,2 2.5,3.5 4.5,4.5 l1.5,-2 l4,2 l-1,3 c-7,0 -12,-5 -12,-12 z"/>
      <text class="contact-line" x="202" y="223">+00 1234 5678 9012</text>

      <path class="contact-icon" d="M173,239 h12 v8 h-12 z M173,239 l6,4.5 l6,-4.5" stroke="var(--card-ink)" stroke-width="0.8"/>
      <text class="contact-line" x="202" y="247">info@email space</text>

      <path class="contact-icon" d="M177,259 l0,11 l2.6,-2.6 l2,4 l1.6,-0.8 l-2,-4 l3.6,0 z"/>
      <text class="contact-line" x="202" y="270">www.websiteaddress</text>
    </g>
  </svg>

</main>
</body>
</html>
```